Dental Learning Allies Needs a Great Looking Sales Brochure!

Please help us design a brochure for our company, Dental Learning Allies, LLC to use for sales and prospecting!
It is our first brochure, and as we are a small company, we don't normally use them, but we have an upcoming meeting and need a GREAT looking brochure with a call to action!
In addition to a pdf print ready version of the file, we need to receive a version with editable pdf text fields.
Our original thought is a 1-page, 4-panel fold or Tri-fold brochure, but we are open to recommendations based on the content.
More about us: We are a small company specializing in education, motivational speaking and event services for dental practices both large and big dental groups. You can check out our website at https://dentallearningallies.example
I have uploaded our logo files, some images for consideration, and proposed text content for the brochure. Note - if you have the space to add our KRV MOTO provider approval we would like to. If you do use the KRV Moto logo, we need to follow their logo guidelines which are also attached.
Should you have any questions, please don't hesitate to ask!
Thank you for helping make us look great!!!!

Target Market(s)

Dental Support Organizations (DSO's)

Font styles to use
Serif
Sans Serif

Requirements
Must have
• Our company logo
• At least 1-2 photos
• Professional look and feel
• Text from uploaded word document for proposed copy
Nice to have
• KRV logo and language showing we are KRV MOTO provider

```html
<!DOCTYPE html>
<html lang="en">
<head>
<meta charset="utf-8">
<title>Dental Learning Allies – Brochure Inside Spread</title>
<link href="https://fonts.googleapis.com/css2?family=Noto+Serif:wght@400;700&family=Open+Sans:ital,wght@0,400;0,600;0,700;1,400&display=swap" rel="stylesheet">
<style>
  :root {
    --backdrop: #dcdcdc;
    --paper: #ffffff;
    --paper-shade: #f1f2f4;
    --ink: #222222;
    --brand-blue: #1f6fc0;
    --deep-blue: #0f4f98;
    --band-black: #0d0d0d;
    --photo-warm: #c9b7a6;
    --photo-cool: #aebfd0;
  }
  * { box-sizing: border-box; margin: 0; padding: 0; }
  html, body { width: 1200px; height: 800px; overflow: hidden; background: var(--backdrop); }
  body { font-family: "Open Sans", Arial, sans-serif; color: var(--ink); }

  .brochure {
    position: absolute; left: 30px; top: 40px;
    width: 1140px; height: 720px;
    display: flex;
    box-shadow: 0 8px 24px rgba(0,0,0,.18);
  }
  .panel {
    position: relative; width: 380px; height: 720px;
    background: linear-gradient(90deg, var(--paper) 0%, var(--paper) 85%, var(--paper-shade) 100%);
    overflow: hidden;
  }
  .panel-art { position: absolute; inset: 0; width: 380px; height: 720px; }

  .panel-heading {
    font-family: "Noto Serif", Georgia, serif;
    color: var(--brand-blue);
    font-weight: 700;
    font-size: 24px;
  }
  .tick-list { list-style: none; }
  .tick-list li {
    position: relative; padding-left: 26px;
    font-size: 15px; line-height: 1.3;
  }
  .tick-list li::before {
    content: ""; position: absolute; left: 4px; top: 3px;
    width: 6px; height: 11px;
    border-right: 2px solid var(--brand-blue);
    border-bottom: 2px solid var(--brand-blue);
    transform: rotate(40deg);
  }

  /* Services panel */
  .services { position: absolute; left: 40px; top: 100px; }
  .services .panel-heading { margin-bottom: 8px; }
  .services li { margin-bottom: 5px; font-size: 16px; }

  /* Why partner panel */
  .partner { position: absolute; left: 34px; top: 80px; width: 320px; }
  .partner .intro { font-size: 15px; margin: 2px 0 10px; }
  .partner li { margin-bottom: 11px; }
  .partner .call-to-action {
    margin-top: 16px; font-size: 18px; line-height: 1.3;
  }

  /* Testimonial panel */
  .testimonial {
    position: absolute; left: 26px; top: 80px; width: 330px;
  }
  .quote-frame {
    position: relative;
    border: 2px solid var(--brand-blue);
    padding: 22px 22px 22px 44px;
    font-size: 14.5px; line-height: 1.45;
  }
  .quote-mark {
    position: absolute; font-family: "Noto Serif", Georgia, serif;
    color: var(--brand-blue); font-size: 62px; font-weight: 700; line-height: 1;
    background: var(--paper); padding: 0 4px;
  }
  .quote-mark.open { left: -14px; top: 4px; }
  .quote-mark.close { right: -14px; bottom: -28px; }
  .attribution { text-align: right; margin-top: 18px; font-size: 14.5px; line-height: 1.35; }
  .attribution .person { color: var(--brand-blue); font-weight: 700; }
</style>
</head>
<body>
<main class="brochure">

  <section class="panel panel-services">
    <svg class="panel-art" viewBox="0 0 380 720" aria-hidden="false">
      <defs>
        <linearGradient id="meetingTones" x1="0" y1="0" x2="1" y2="1">
          <stop offset="0" stop-color="#e6e9ee"/>
          <stop offset="0.5" stop-color="var(--photo-cool)"/>
          <stop offset="1" stop-color="#7d8ea4"/>
        </linearGradient>
        <radialGradient id="clipboardTones" cx="0.55" cy="0.45" r="0.6">
          <stop offset="0" stop-color="#eee7e1"/>
          <stop offset="1" stop-color="var(--photo-warm)"/>
        </radialGradient>
      </defs>
      <path d="M0 0H380V36Q190 -4 0 70Z" fill="var(--band-black)"/>
      <line x1="0" y1="330" x2="380" y2="520" stroke="var(--brand-blue)" stroke-width="1.5"/>
      <g role="img" aria-label="Photo of a video conference meeting with a team seated at a table">
        <path d="M0 470Q200 520 380 520V700H0Z" fill="url(#meetingTones)"/>
      </g>
      <path d="M0 470Q200 520 380 520" fill="none" stroke="var(--brand-blue)" stroke-width="4"/>
      <g role="img" aria-label="Photo of a hand holding a clipboard during a training session">
        <circle cx="165" cy="380" r="88" fill="url(#clipboardTones)" stroke="var(--band-black)" stroke-width="8"/>
      </g>
      <rect x="0" y="700" width="380" height="20" fill="var(--brand-blue)"/>
    </svg>
    <div class="services">
      <h2 class="panel-heading">Services</h2>
      <ul class="tick-list">
        <li>Clinical Training</li>
        <li>Web-Based Learning</li>
        <li>Chairside Coaching</li>
        <li>Train Your Trainer</li>
        <li>Regional or Annual Meetings</li>
        <li>Metric Analytics</li>
      </ul>
    </div>
  </section>

  <section class="panel panel-partner">
    <svg class="panel-art" viewBox="0 0 380 720">
      <defs>
        <linearGradient id="classroomTones" x1="0" y1="0" x2="1" y2="0">
          <stop offset="0" stop-color="#cdd6df"/>
          <stop offset="0.5" stop-color="var(--photo-warm)"/>
          <stop offset="1" stop-color="#d8cfc4"/>
        </linearGradient>
      </defs>
      <path d="M0 0H380V40Q190 -10 0 36Z" fill="var(--band-black)"/>
      <g role="img" aria-label="Photo of smiling students gathered around a teacher in a classroom">
        <path d="M0 565Q190 540 380 545V700H0Z" fill="url(#classroomTones)"/>
      </g>
      <path d="M0 565Q190 540 380 545" fill="none" stroke="var(--brand-blue)" stroke-width="4"/>
      <rect x="0" y="700" width="380" height="20" fill="var(--brand-blue)"/>
    </svg>
    <div class="partner">
      <h2 class="panel-heading">Why partner with us?</h2>
      <p class="intro">Do you want to:</p>
      <ul class="tick-list">
        <li>Make hygiene the driver of every dental practice?</li>
        <li>Consistently achieve production goals?</li>
        <li>Provide excellent care for every patient in every practice?</li>
        <li>Provide continuity of care between providers?</li>
        <li>Standardize scripting to increase treatment enrollment?</li>
        <li>Improve the retention of both your staff and your patients?</li>
        <li>Supplement your education initiatives with metrics-based needs assessment?</li>
      </ul>
      <p class="call-to-action">If you said yes to any of these questions, then DLA is right for you!</p>
    </div>
  </section>

  <section class="panel panel-testimonial">
    <svg class="panel-art" viewBox="0 0 380 720">
      <defs>
        <linearGradient id="audienceTones" x1="0" y1="0" x2="1" y2="1">
          <stop offset="0" stop-color="#e9ecef"/>
          <stop offset="0.55" stop-color="var(--photo-warm)"/>
          <stop offset="1" stop-color="#8b7766"/>
        </linearGradient>
      </defs>
      <path d="M0 0H380V55Q190 -10 0 40Z" fill="var(--band-black)"/>
      <g role="img" aria-label="Photo of an audience raising hands during a presentation">
        <path d="M0 560Q240 520 380 290V700H0Z" fill="url(#audienceTones)"/>
      </g>
      <path d="M0 560Q240 520 380 290" fill="none" stroke="var(--brand-blue)" stroke-width="4"/>
      <rect x="0" y="700" width="380" height="20" fill="var(--brand-blue)"/>
    </svg>
    <div class="testimonial">
      <blockquote class="quote-frame">
        <span class="quote-mark open">“</span>
        Dental Learning Allies delivered training for our team that isn’t offered anywhere else. Their training has dramatically changed our team’s ability to influence treatment acceptance. I would recommend their services to any DSO looking to increase profitability!
        <span class="quote-mark close">”</span>
      </blockquote>
      <p class="attribution">
        <span class="person">Dr. Martin Halvorsen,</span><br>
        Chief Clinical Officer,<br>
        Bright Harbor Practice Group
      </p>
    </div>
  </section>

</main>
</body>
</html>
```